A start-up named "trovamind" - a clinical research organization needs a new PowerPoint design

We need a new PowerPoint Design (incl. business card and stationery design) for an early-stage start-up named "trovamind" seeking to build an ecosystem/ strategic partner alliances or consortium of committed and active collaborators to guide important components of the clinical trial.

Our ultimate goal is to avoid false neutrals – therapies that have not been and may never be evaluated in clinical trials due to the costs and/ or complexity.

The final design should highlight our patient-centric approach, innovative study design supported with the novel AI platform to make a stronger impact on patient lives.

Please see the attached brief for more details.
Updates

Requesting the proposals on color-coding, business-card designs, clinical research visuals, and icons as well as stationery design.

Target Market(s)

Pharma/ Biotech Executives
Medical Institutions
Clinical Trial Participants (Patients)

Colors
e34398

Requirements
Must have
• Use the Color Version of purple/ magenta logo

```html
<!DOCTYPE html>
<html lang="en">
<head>
<meta charset="utf-8">
<title>trovamind – presentation design</title>
<link href="https://fonts.googleapis.com/css2?family=Poppins:wght@400;600;700;800&display=swap" rel="stylesheet">
<style>
  :root {
    --page-bg: #48484a;
    --slide-bg: #f2f2f2;
    --brand: #3346c9;
    --heading-blue: #2c52c4;
    --ink: #141414;
    --body: #3d3d3d;
    --accent: #6a2fc9;
  }
  * { margin: 0; padding: 0; box-sizing: border-box; }
  html, body { width: 1200px; height: 4139px; overflow: hidden; }
  body { background: var(--page-bg); font-family: 'Poppins', sans-serif; position: relative; }

  .slide { position: absolute; left: 84px; width: 1024px; height: 768px; background: var(--slide-bg); overflow: hidden; }
  .slide-cover { top: 72px; }
  .slide-about { top: 878px; }
  .slide-grid { top: 1677px; }
  .slide-list { top: 2475px; }
  .slide-feature { top: 3286px; }

  .wordmark { position: absolute; display: flex; align-items: center; gap: 12px; color: var(--brand); font-weight: 700; letter-spacing: -1px; line-height: 1; }
  .wordmark .mark { display: block; background: var(--accent); }
  .wordmark-small { font-size: 52px; }
  .wordmark-small .mark { width: 20px; height: 20px; }
  .wordmark-large { font-size: 96px; left: 50%; top: 318px; transform: translateX(-50%); }
  .wordmark-large .mark { width: 34px; height: 34px; }

  .slide-title { position: absolute; right: 60px; top: 34px; font-size: 34px; font-weight: 800; color: var(--heading-blue); letter-spacing: -0.5px; }

  .photo { position: absolute; }

  .item-title { font-size: 16px; font-weight: 700; color: var(--ink); letter-spacing: -0.2px; text-transform: uppercase; }
  .item-body { font-size: 14.5px; line-height: 22px; color: var(--body); margin-top: 10px; }
  .item { position: absolute; width: 400px; }

  .about-copy { position: absolute; left: 532px; top: 152px; width: 440px; }
  .about-copy .lead { font-size: 22px; line-height: 30px; font-weight: 700; color: var(--ink); text-transform: uppercase; letter-spacing: -0.3px; }
  .about-copy .item-body { margin-top: 18px; font-size: 14px; line-height: 22px; }

  .list-item { position: absolute; left: 559px; width: 430px; padding-left: 37px; }
  .list-item svg { position: absolute; left: 0; top: 4px; }

  .feature-panel { position: absolute; left: 0; top: 0; width: 665px; height: 601px; background: var(--slide-bg); }
  .feature-block { position: absolute; left: 31px; width: 590px; }
  .feature-block .item-title { font-size: 22px; }
  .feature-block .item-body { font-size: 17px; line-height: 22px; margin-top: 8px; }
</style>
</head>
<body>

<section class="slide slide-cover">
  <div class="wordmark wordmark-large"><span>trovamind</span><span class="mark"></span></div>
</section>

<section class="slide slide-about">
  <div class="wordmark wordmark-small" style="left:18px;top:42px;"><span>trovamind</span><span class="mark"></span></div>
  <h2 class="slide-title">ABOUT US</h2>
  <div class="photo" role="img" aria-label="Scientist in protective suit and mask holding a test tube in a laboratory" style="left:0;top:193px;width:483px;height:575px;background:linear-gradient(135deg,#e0702a 0%,#b8623c 20%,#3a4f86 50%,#1d3566 80%,#0f1e3e 100%);"></div>
  <div class="about-copy">
    <p class="lead">On the other hand, we denounce with righteous indignation and dislike men</p>
    <p class="item-body">On the other hand, we denounce with righteous indignation and dislike men who are so beguiled and demoralized by the charms of pleasure of the moment, so blinded by desire, that they cannot foresee the pain and trouble that are bound to ensue; and equal blame belongs to those who fail in their duty through weakness of will, which is the same as saying through shrinking from toil and pain. These cases are perfectly simple and easy to distinguish. In a free hour, when our power of choice is untrammelled and when nothing prevents our being able to do what we like best, every pleasure is to be welcomed and every pain avoided. But in certain circumstances and owing to the claims of duty or the obligations of business it will frequently occur that pleasures have to be repudiated and annoyances accepted. The wise man therefore always holds in these matters to this principle of selection: he rejects pleasures to secure other greater pleasures, or else he endures pains to avoid worse pains</p>
  </div>
</section>

<section class="slide slide-grid">
  <div class="wordmark wordmark-small" style="left:56px;top:46px;"><span>trovamind</span><span class="mark"></span></div>
  <h2 class="slide-title" style="right:44px;">HEADING</h2>
  <div class="item" style="left:55px;top:170px;"><h3 class="item-title">Lorem ipsum is simply dummy text</h3><p class="item-body">At vero eos et accusamus et iusto odio dignissimos ducimus qui blanditiis praesentium voluptatum deleniti atque corrupti quos dolores et quas molestias excepturi sint occaecati cupiditate non provident,</p></div>
  <div class="item" style="left:559px;top:170px;"><h3 class="item-title">Lorem ipsum is simply dummy text</h3><p class="item-body">At vero eos et accusamus et iusto odio dignissimos ducimus qui blanditiis praesentium voluptatum deleniti atque corrupti quos dolores et quas molestias excepturi sint occaecati cupiditate non provident,</p></div>
  <div class="item" style="left:55px;top:355px;"><h3 class="item-title">Lorem ipsum is simply dummy text</h3><p class="item-body">At vero eos et accusamus et iusto odio dignissimos ducimus qui blanditiis praesentium voluptatum deleniti atque corrupti quos dolores et quas molestias excepturi sint occaecati cupiditate non provident,</p></div>
  <div class="item" style="left:55px;top:550px;"><h3 class="item-title">Lorem ipsum is simply dummy text</h3><p class="item-body">At vero eos et accusamus et iusto odio dignissimos ducimus qui blanditiis praesentium voluptatum deleniti atque corrupti quos dolores et quas molestias excepturi sint occaecati cupiditate non provident,</p></div>
  <div class="photo" role="img" aria-label="Close-up of laboratory microscope objectives over a glowing slide, gloved hands either side" style="left:483px;top:327px;width:541px;height:441px;background:linear-gradient(160deg,#c9d6e6 0%,#5d7598 35%,#2a4a86 65%,#15305e 100%);"></div>
</section>

<section class="slide slide-list">
  <div class="wordmark wordmark-small" style="left:18px;top:42px;"><span>trovamind</span><span class="mark"></span></div>
  <h2 class="slide-title">HEADING</h2>
  <div class="photo" role="img" aria-label="Researchers in masks working at a lab bench" style="left:22px;top:159px;width:283px;height:294px;background:linear-gradient(135deg,#2b4c7e,#8ba6c8 55%,#e8eef5);"></div>
  <div class="photo" role="img" aria-label="Open hands beneath floating medical icons" style="left:344px;top:234px;width:179px;height:174px;background:linear-gradient(160deg,#aebfd9,#dfe6f0 60%,#c9a999);"></div>
  <div class="photo" role="img" aria-label="Three scientists in lab coats reviewing samples" style="left:30px;top:474px;width:180px;height:172px;background:linear-gradient(160deg,#e9ecef,#cfd8e2 50%,#7d95b4);"></div>
  <div class="photo" role="img" aria-label="Scientist looking through a microscope" style="left:228px;top:426px;width:304px;height:295px;background:linear-gradient(135deg,#4d5460,#a9b0b9 45%,#eef0f2);"></div>

  <div class="list-item" style="top:167px;"><svg width="14" height="22" viewBox="0 0 14 22"><path d="M3 3l8 8-8 8" fill="none" stroke="#2b2f4a" stroke-width="2.5"/></svg><h3 class="item-title">Lorem ipsum is simply dummy text</h3><p class="item-body" style="margin-top:6px;">At vero eos et accusamus et iusto odio dignissimos ducimus qui blanditiis praesentium voluptatum deleniti atque corrupti quos dolores et quas molestias excepturi sint occaecati cupiditate non provident,</p></div>
  <div class="list-item" style="top:315px;"><svg width="14" height="22" viewBox="0 0 14 22"><path d="M3 3l8 8-8 8" fill="none" stroke="#2b2f4a" stroke-width="2.5"/></svg><h3 class="item-title">Lorem ipsum is simply dummy text</h3><p class="item-body" style="margin-top:6px;">At vero eos et accusamus et iusto odio dignissimos ducimus qui blanditiis praesentium voluptatum deleniti atque corrupti quos dolores et quas molestias excepturi sint occaecati cupiditate non provident,</p></div>
  <div class="list-item" style="top:471px;"><svg width="14" height="22" viewBox="0 0 14 22"><path d="M3 3l8 8-8 8" fill="none" stroke="#2b2f4a" stroke-width="2.5"/></svg><h3 class="item-title">Lorem ipsum is simply dummy text</h3><p class="item-body" style="margin-top:6px;">At vero eos et accusamus et iusto odio dignissimos ducimus qui blanditiis praesentium voluptatum deleniti atque corrupti quos dolores et quas molestias excepturi sint occaecati cupiditate non provident,</p></div>
  <div class="list-item" style="top:623px;"><svg width="14" height="22" viewBox="0 0 14 22"><path d="M3 3l8 8-8 8" fill="none" stroke="#2b2f4a" stroke-width="2.5"/></svg><h3 class="item-title">Lorem ipsum is simply dummy text</h3><p class="item-body" style="margin-top:6px;">At vero eos et accusamus et iusto odio dignissimos ducimus qui blanditiis praesentium voluptatum deleniti atque corrupti quos dolores et quas molestias excepturi sint occaecati cupiditate non provident,</p></div>
</section>

<section class="slide slide-feature">
  <div class="photo" role="img" aria-label="Smiling scientist in safety glasses and gloves holding a sample tube in a lab" style="left:313px;top:127px;width:711px;height:641px;background:linear-gradient(120deg,#8a7a6c 0%,#d8d4cf 40%,#f3f4f5 60%,#c6cdd6 85%,#7fd6c0 100%);"></div>
  <div class="feature-panel"></div>
  <div class="wordmark wordmark-small" style="left:37px;top:38px;"><span>trovamind</span><span class="mark"></span></div>
  <h2 class="slide-title" style="right:37px;">HEADING</h2>
  <div class="feature-block" style="top:143px;"><h3 class="item-title">Lorem ipsum is simply dummy text</h3><p class="item-body">At vero eos et accusamus et iusto odio dignissimos ducimus qui blanditiis praesentium voluptatum deleniti atque corrupti quos dolores et quas molestias excepturi sint occaecati cupiditate non provident, similique sunt in culpa qui officia deserunt mollitia animi, id est laborum et dolorum fuga. Et harum quidem rerum facilis est et expedita distinctio. Nam libero tempore, cum soluta nobis est eligendi optio cumque nihil impedit quo minus id quod maxim</p></div>
  <div class="feature-block" style="top:384px;"><h3 class="item-title">On the other hand, we denounce</h3><p class="item-body">At vero eos et accusamus et iusto odio dignissimos ducimus qui blanditiis praesentium voluptatum deleniti atque corrupti quos dolores et quas molestias excepturi sint occaecati cupiditate non provident, similique sunt in culpa qui officia deserunt mollitia animi, id est laborum et dolorum fuga. Et harum quidem rerum facilis est et expedita distinctio. Nam libero tempore, cum soluta nobis est eligendi optio cumque nihil impedit quo minus id quod maxim</p></div>
</section>

</body>
</html>
```